Wine Label for a White and a Red Wine from Italy

We have a very good idea of what we want with artwork. We need you to please design a 'template' with the text so we can change out the artwork from year to year. Samples are shown of what we are looking for. We are looking for options with the two basic designs. Brand name of wine is: Valora di Castegno. Both wines are in a light green Bordeaux-style bottle (note: we don't show a light green bottle in the mockup but please remember the bottle is light green). Artwork is provided. We'd like to see either the green or blue butterfly on the white wine, the red butterfly is for the red wine. Please base the design on the attached label from Brailey and/or the attached label from Chateau Mervanges.

Target Market(s)

Millennials, women

Requirements
Must have
• The artwork (butterflies) attached.
Nice to have
• Elegant, readable fonts. Please make the text so it can be changed by the printer. Please make it so the artwork can be changed too.

```html
<!DOCTYPE html>
<html lang="en">
<head>
<meta charset="utf-8">
<title>Valora di Castegno – Barrel Select Rosso Label</title>
<link rel="stylesheet" href="https://fonts.googleapis.com/css2?family=Cormorant+Garamond:ital,wght@0,400;1,400&family=Montserrat:wght@300;400&family=Allura&display=swap">
<style>
  :root {
    --paper: #ffffff;
    --ink: #1a1a1a;
    --ink-soft: #333333;
    --frame: #b9b9b9;
    --art-gold: #f2b01e;
    --art-amber: #e58a12;
    --art-pale: #f7d67a;
    --art-teal: #1f8f94;
  }
  * { margin: 0; padding: 0; box-sizing: border-box; }
  html, body {
    width: 1200px;
    height: 622px;
    overflow: hidden;
    background: var(--paper);
  }
  .label {
    position: relative;
    width: 1200px;
    height: 622px;
    background: var(--paper);
    border: 1px solid var(--frame);
    overflow: hidden;
  }
  .label__artwork {
    position: absolute;
    inset: 0;
    width: 1200px;
    height: 622px;
  }
  .label__text {
    position: absolute;
    left: 374px;
    width: 400px;
    text-align: center;
    color: var(--ink);
    white-space: nowrap;
  }
  .brand-name {
    top: 70px;
    font-family: "Cormorant Garamond", Georgia, serif;
    font-style: italic;
    font-size: 66px;
    line-height: 1;
  }
  .brand-sub {
    top: 146px;
    font-family: "Cormorant Garamond", Georgia, serif;
    font-style: italic;
    font-size: 28px;
    line-height: 1;
  }
  .cuvee {
    top: 218px;
    font-family: "Montserrat", Arial, sans-serif;
    font-weight: 300;
    font-size: 18px;
    letter-spacing: 0.42em;
    padding-left: 0.42em;
    line-height: 1;
  }
  .wine-details {
    top: 304px;
    font-family: "Cormorant Garamond", Georgia, serif;
    font-size: 24px;
    line-height: 33px;
  }
  .divider {
    position: absolute;
    left: 566px;
    top: 439px;
    width: 16px;
    height: 1px;
    background: var(--ink-soft);
  }
  .producer {
    top: 479px;
    font-family: "Montserrat", Arial, sans-serif;
    font-weight: 400;
    font-size: 15.5px;
    color: var(--ink-soft);
    line-height: 1;
  }
  .farming {
    top: 514px;
    font-family: "Allura", "Brush Script MT", cursive;
    font-size: 34px;
    line-height: 1;
  }
</style>
</head>
<body>
  <main class="label">
    <svg class="label__artwork" viewBox="0 0 1200 622" xmlns="http://www.w3.org/2000/svg">
      <defs>
        <linearGradient id="artwork-left-tone" x1="0" y1="0" x2="1" y2="1">
          <stop offset="0" stop-color="var(--art-gold)"/>
          <stop offset="0.35" stop-color="var(--art-amber)"/>
          <stop offset="0.6" stop-color="var(--art-teal)" stop-opacity="0.55"/>
          <stop offset="1" stop-color="var(--art-pale)"/>
        </linearGradient>
        <linearGradient id="artwork-right-tone" x1="1" y1="0" x2="0" y2="1">
          <stop offset="0" stop-color="var(--art-pale)"/>
          <stop offset="0.3" stop-color="var(--art-gold)"/>
          <stop offset="0.6" stop-color="var(--art-teal)" stop-opacity="0.6"/>
          <stop offset="1" stop-color="var(--art-amber)"/>
        </linearGradient>
      </defs>
      <polygon class="artwork-panel artwork-panel--left"
               role="img" aria-label="Painted artwork: teal butterfly on brushed gold and amber strokes"
               points="0,0 515,0 362,622 0,622" fill="url(#artwork-left-tone)"/>
      <polygon class="artwork-panel artwork-panel--right"
               role="img" aria-label="Painted artwork: teal butterflies on brushed gold and amber strokes"
               points="892,0 1200,0 1200,622 742,622" fill="url(#artwork-right-tone)"/>
    </svg>

    <h1 class="label__text brand-name">Valora</h1>
    <p class="label__text brand-sub">di Castegno</p>
    <p class="label__text cuvee">BARREL SELECT</p>
    <p class="label__text wine-details">2018<br>Rosso<br>Piemonte, Italy</p>
    <span class="divider"></span>
    <p class="label__text producer">Artisanlly Crafted by Cantina Due Colli</p>
    <p class="label__text farming">Sustainably Farmed</p>
  </main>
</body>
</html>
```